Detox Before & After Charts

I am looking to create a chart/graph to be used to chart a patient's progress before and after using our 15-day detox program. We will be looking for 3 different graphs to be made.
1. A chart showing the before and after symptom scores of 12 patients in a small clinical trial we did. We will use this one to show prospective patients.
2. A chart showing one single patient's "total" symptom scores before and after the detox. We will use this with each patient, before and after they do the detox.
3. A chart showing one patient's before and symptom scores in more detail, showing their scores in each one of the symptom categories. We will do this with each patient, before and after the detox.
For #2 & #3 above, we would want a master template that we could add the scoring for each new patient ourselves.
See attached for rough samples.
Each of these 3 charts should be the same style, but for now, just do chart #3. And after we decide on the designer, then we will have them do the other 2 charts.
And I prefer a line graph over a bar graph for these. I did not mention that at first. Sorry!!

```html
<!DOCTYPE html>
<html lang="en">
<head>
<meta charset="utf-8">
<title>One Patient Before &amp; After</title>
<link rel="stylesheet" href="https://fonts.googleapis.com/css2?family=Questrial&family=Open+Sans:wght@400;700&display=swap">
<style>
  :root {
    --paper: #ffffff;
    --ink: #222222;
    --muted: #444444;
    --before: #2f6eb5;
    --before-line: #5b9bd5;
    --after: #c55a11;
    --after-line: #ed7d31;
    --change: #d9d9d9;
    --grid: #d9d9d9;
    --axis: #333333;
    --panel-top: #dde8f3;
    --panel-bottom: #fdf0cf;
  }
  * { box-sizing: border-box; margin: 0; padding: 0; }
  html, body { width: 1200px; height: 1000px; overflow: hidden; background: var(--paper); }
  .sheet {
    position: absolute; left: 7px; top: 41px;
    width: 912px; height: 706px;
    transform: scale(1.3); transform-origin: 0 0;
    font-family: "Questrial", sans-serif; color: var(--ink);
  }
  .field { position: absolute; top: 84px; font-size: 13px; display: flex; align-items: flex-end; letter-spacing: -0.3px; }
  .field .rule { border-bottom: 1px solid var(--ink); height: 14px; margin-left: 3px; }
  .field-first { left: 83px; }
  .field-first .rule { width: 304px; }
  .field-last { left: 465px; }
  .field-last .rule { width: 294px; }
  .date { position: absolute; top: 114px; font-size: 8px; transform: translateX(-50%); }
  .summary {
    position: absolute; left: 83px; top: 140px; width: 762px;
    border-collapse: collapse; font-size: 11px;
  }
  .summary th, .summary td { border: 1px solid var(--ink); height: 29px; font-weight: 400; }
  .summary thead th { height: 31px; border-width: 3px 1px 1px 1px; }
  .summary thead th:first-child { border: none; border-right: 3px solid var(--ink); background: transparent; }
  .summary thead th:last-child, .summary tbody td:last-child { border-right-width: 3px; }
  .summary tbody tr:last-child td, .summary tbody tr:last-child th { border-bottom-width: 3px; }
  .summary tbody th { border-left-width: 3px; text-align: left; padding-left: 6px; width: 190px; }
  .summary tbody td:nth-child(2) { border-left-width: 3px; }
  .summary .col-before { background: var(--before); color: #fff; width: 190px; }
  .summary .col-after { background: var(--after); color: #fff; width: 190px; }
  .summary .col-change { background: var(--change); }
  .chart { position: absolute; left: 54px; top: 251px; width: 812px; height: 354px; display: block; }
  .chart-title { font-family: "Open Sans", sans-serif; font-weight: 700; font-size: 16px; fill: #404040; }
  .axis-title { font-family: "Questrial", sans-serif; font-size: 9px; fill: var(--muted); }
  .category { font-family: "Open Sans", sans-serif; font-weight: 700; font-size: 7.5px; fill: #333; }
  .point-label { font-family: "Open Sans", sans-serif; font-weight: 700; font-size: 7px; fill: #fff; }
  .series-before .dot { fill: var(--before-line); }
  .series-after .dot { fill: var(--after-line); }
</style>
</head>
<body>
<main class="sheet">
  <div class="field field-first">First Name:<span class="rule"></span></div>
  <div class="field field-last">Last Name:<span class="rule"></span></div>
  <span class="date" style="left:369px">6/1/2018</span>
  <span class="date" style="left:559px">6/18/2018</span>

  <table class="summary">
    <thead>
      <tr><th></th><th class="col-before">BEFORE</th><th class="col-after">AFTER</th><th class="col-change">Change</th></tr>
    </thead>
    <tbody>
      <tr><th>TOTAL SYMPTOM SCORE</th><td></td><td></td><td></td></tr>
      <tr><th>WEIGHT</th><td></td><td></td><td></td></tr>
    </tbody>
  </table>

  <svg class="chart" viewBox="54 251 812 354" xmlns="http://www.w3.org/2000/svg">
    <defs>
      <linearGradient id="panel-fill" x1="0" y1="0" x2="0" y2="1">
        <stop offset="0" stop-color="var(--panel-top)"/>
        <stop offset="1" stop-color="var(--panel-bottom)"/>
      </linearGradient>
    </defs>
    <rect x="54" y="251" width="812" height="354" fill="url(#panel-fill)"/>
    <text class="chart-title" x="460" y="279" text-anchor="middle">ONE PATIENT BEFORE &amp; AFTER</text>

    <g class="gridlines" stroke="var(--grid)" stroke-width="1">
      <line x1="113" y1="345" x2="853" y2="345"/>
      <line x1="113" y1="392" x2="853" y2="392"/>
      <line x1="113" y1="438" x2="853" y2="438"/>
      <line x1="113" y1="485" x2="853" y2="485"/>
      <line x1="113" y1="531" x2="853" y2="531"/>
    </g>
    <line x1="113" y1="578" x2="853" y2="578" stroke="var(--axis)" stroke-width="1.5"/>

    <g class="axis-title" transform="rotate(-90)" text-anchor="middle">
      <text x="-431" y="82">CATEGORY</text>
      <text x="-431" y="92">SYMPTOM</text>
      <text x="-431" y="102">% SCORE</text>
    </g>

    <g class="categories" text-anchor="middle">
      <text class="category" x="139" y="594">DIGESTION</text>
      <text class="category" x="192" y="594">EMOTION</text>
      <text class="category" x="245" y="594">EYES</text>
      <text class="category" x="298" y="594">LUNGS</text>
      <text class="category" x="351" y="594">MIND</text>
      <text class="category" x="404" y="594">ENERGY</text>
      <text class="category" x="457" y="594">HEAD</text>
      <text class="category" x="510" y="594">EARS</text>
      <text class="category" x="563" y="594">MOUTH</text>
      <text class="category" x="615" y="594">SKIN</text>
      <text class="category" x="668" y="594">PAIN</text>
      <text class="category" x="721" y="594">NOSE</text>
      <text class="category" x="774" y="594">HEART</text>
      <text class="category" x="827" y="594">WEIGHT</text>
    </g>

    <g class="series-before">
      <polyline fill="none" stroke="var(--before-line)" stroke-width="2.5" stroke-linejoin="round"
        points="139,550 192,506 245,520 298,550 351,550 404,550 457,492 510,550 563,531 615,473 668,345 721,508 774,520 827,569"/>
      <g class="dot">
        <circle cx="139" cy="550" r="9"/><circle cx="192" cy="506" r="9"/><circle cx="245" cy="520" r="9"/>
        <circle cx="298" cy="550" r="9"/><circle cx="351" cy="550" r="9"/><circle cx="404" cy="550" r="9"/>
        <circle cx="457" cy="492" r="9"/><circle cx="510" cy="550" r="9"/><circle cx="563" cy="531" r="9"/>
        <circle cx="615" cy="473" r="9"/><circle cx="668" cy="345" r="9"/><circle cx="721" cy="508" r="9"/>
        <circle cx="774" cy="520" r="9"/><circle cx="827" cy="569" r="9"/>
      </g>
      <g text-anchor="middle">
        <text class="point-label" x="192" y="508.5">31</text><text class="point-label" x="245" y="522.5">25</text>
        <text class="point-label" x="298" y="552.5">12</text><text class="point-label" x="351" y="552.5">12</text>
        <text class="point-label" x="404" y="552.5">12</text><text class="point-label" x="457" y="494.5">37</text>
        <text class="point-label" x="510" y="552.5">12</text><text class="point-label" x="563" y="533.5">20</text>
        <text class="point-label" x="615" y="475.5">45</text><text class="point-label" x="668" y="347.5">100</text>
        <text class="point-label" x="721" y="510.5">30</text><text class="point-label" x="774" y="522.5">25</text>
        <text class="point-label" x="827" y="571.5">4</text>
      </g>
    </g>

    <g class="series-after">
      <polyline fill="none" stroke="var(--after-line)" stroke-width="2.5" stroke-linejoin="round"
        points="139,550 192,578 245,578 298,578 351,578 404,564 457,578 510,578 563,566 615,555 668,543 721,566 774,578 827,578"/>
      <g class="dot">
        <circle cx="139" cy="550" r="9"/><circle cx="192" cy="578" r="9"/><circle cx="245" cy="578" r="9"/>
        <circle cx="298" cy="578" r="9"/><circle cx="351" cy="578" r="9"/><circle cx="404" cy="564" r="9"/>
        <circle cx="457" cy="578" r="9"/><circle cx="510" cy="578" r="9"/><circle cx="563" cy="566" r="9"/>
        <circle cx="615" cy="555" r="9"/><circle cx="668" cy="543" r="9"/><circle cx="721" cy="566" r="9"/>
        <circle cx="774" cy="578" r="9"/><circle cx="827" cy="578" r="9"/>
      </g>
      <g text-anchor="middle">
        <text class="point-label" x="139" y="552.5">12</text><text class="point-label" x="192" y="580.5">0</text>
        <text class="point-label" x="245" y="580.5">0</text><text class="point-label" x="298" y="580.5">0</text>
        <text class="point-label" x="351" y="580.5">0</text><text class="point-label" x="404" y="566.5">6</text>
        <text class="point-label" x="457" y="580.5">0</text><text class="point-label" x="510" y="580.5">0</text>
        <text class="point-label" x="563" y="568.5">5</text><text class="point-label" x="615" y="557.5">10</text>
        <text class="point-label" x="668" y="545.5">15</text><text class="point-label" x="721" y="568.5">5</text>
        <text class="point-label" x="774" y="580.5">0</text><text class="point-label" x="827" y="580.5">0</text>
      </g>
    </g>
  </svg>
</main>
</body>
</html>
```